New Wine Brand bottle label-LumaBrio

We need a label designed for a new wine. The label should catch the customers eye with colors. It will be a red wine. We need a design that makes the customer think the wine has nutritional value and is unique when compared to other wines in that regard. Think: energized, vitality, healthy. Name of wine is LumaBrio

Target Market(s)

PPL aged 21-50 looking for healthy alternatives/supplements

Colors

Designer to choose colors to be used in the design.

Requirements
Must have
• eye catching label

```html
<!DOCTYPE html>
<html lang="en">
<head>
<meta charset="utf-8">
<title>LumaBrio Red Wine Label</title>
<link rel="stylesheet" href="https://fonts.googleapis.com/css2?family=Josefin+Sans:wght@600;700&display=swap">
<style>
  :root {
    --page: #ffffff;
    --label-black: #000000;
    --band-maroon: #3a0303;
    --name-white: #ffffff;
    --name-glow: rgba(255, 170, 90, 0.75);
    --wine-red: #e0101a;
    --wine-red-dark: #8a0008;
    --art-red: #d8141c;
    --art-gold: #f0a040;
    --info-white: #ffffff;
  }
  * { margin: 0; padding: 0; box-sizing: border-box; }
  html, body {
    width: 1200px;
    height: 1200px;
    overflow: hidden;
    background: var(--page);
  }
  .canvas {
    position: relative;
    width: 1200px;
    height: 1200px;
  }
  .label {
    position: absolute;
    left: 212px;
    top: 50px;
    width: 776px;
    height: 1100px;
    background: var(--label-black);
    overflow: hidden;
    font-family: "Josefin Sans", sans-serif;
  }
  .label__band {
    position: absolute;
    left: 0;
    top: 0;
    width: 100%;
    height: 254px;
    background: var(--band-maroon);
    display: flex;
    align-items: center;
    justify-content: center;
  }
  .label__name {
    color: var(--name-white);
    font-weight: 700;
    font-size: 128px;
    letter-spacing: 2px;
    line-height: 1;
    padding-top: 18px;
    text-shadow: 0 0 10px var(--name-glow), 0 0 22px rgba(255, 120, 40, 0.45);
  }
  .label__art {
    position: absolute;
    left: 0;
    top: 360px;
    width: 100%;
    height: 540px;
  }
  .label__variety {
    position: absolute;
    left: 0;
    top: 780px;
    width: 100%;
    text-align: center;
    font-weight: 700;
    font-size: 124px;
    line-height: 1;
    letter-spacing: 1px;
    color: var(--wine-red);
    -webkit-text-stroke: 3px var(--wine-red-dark);
    text-shadow: -5px 4px 0 #1a0000;
  }
  .label__info {
    position: absolute;
    left: 0;
    top: 990px;
    width: 100%;
    text-align: center;
    color: var(--info-white);
    font-weight: 600;
    font-size: 35px;
    line-height: 48px;
    letter-spacing: 2px;
  }
</style>
</head>
<body>
  <main class="canvas">
    <section class="label">
      <header class="label__band">
        <h1 class="label__name">LUMABRIO</h1>
      </header>

      <svg class="label__art" viewBox="0 0 776 540" role="img" aria-label="Abstract artwork of red diagonal capsule shapes crossed by swirling golden light trails and sparkles">
        <defs>
          <radialGradient id="art-glow" cx="55%" cy="45%" r="60%">
            <stop offset="0%" stop-color="#e8201e"/>
            <stop offset="45%" stop-color="#a80c14"/>
            <stop offset="100%" stop-color="#000000" stop-opacity="0"/>
          </radialGradient>
          <linearGradient id="art-trail" x1="0" y1="0" x2="1" y2="0">
            <stop offset="0%" stop-color="#f0a040" stop-opacity="0"/>
            <stop offset="50%" stop-color="#f0a040" stop-opacity="0.45"/>
            <stop offset="100%" stop-color="#f0a040" stop-opacity="0"/>
          </linearGradient>
        </defs>
        <rect x="0" y="0" width="776" height="540" fill="url(#art-glow)"/>
        <rect x="0" y="90" width="776" height="150" fill="url(#art-trail)"/>
      </svg>

      <h2 class="label__variety">RED WINE</h2>

      <p class="label__info">0,75 L<br>16% ALC/VOL</p>
    </section>
  </main>
</body>
</html>
```